hotel's Website

Hotels website redesign for reference pictures, logo etc see http://restwellmarlow.co.uk/

1. 2-3 Special offers on the main page.
2. Booking calender
3. Location Map
4. Picture gallery.
5. Journeyscope reviews.
6. short description
7. Social Media sharing.
8 Phone number and address.

Industry/Entity Type

Hotel

Requirements
Must have
• 1. 2-3 Special offers on the main page.
2. Booking calender
3. Location Map
4. Picture gallery.
5. Journeyscope reviews.
6. short description
7. Social Media sharing.

```html
<!DOCTYPE html>
<html lang="en">
<head>
<meta charset="utf-8">
<title>Restwell Inn – London Victoria</title>
<link rel="stylesheet" href="https://fonts.googleapis.com/css2?family=Open+Sans:wght@400;600;700&family=Ubuntu:wght@500;700&display=swap">
<style>
:root{
  --navy:#1e4a70;
  --header:#2e6394;
  --topbar:#244f78;
  --orange:#e97a22;
  --welcome-orange:#d9762f;
  --link-blue:#1f4b7a;
  --yellow:#f3ad1c;
  --text:#555;
  --band:#e9e6e3;
  --gallery-bg:#f3f2f2;
  --footer:#1d1d1d;
  --input:#e3e3e3;
  --frame:#d9d9d9;
}
*{box-sizing:border-box;margin:0;padding:0}
html,body{width:989px;height:1200px;overflow:hidden;background:#fff}
body{font-family:"Open Sans",Arial,sans-serif;color:var(--text)}
.page{position:relative;width:989px;height:1200px;overflow:hidden}
.abs{position:absolute}

.top-bar{left:0;top:0;width:989px;height:30px;background:var(--topbar);color:#fff;font-size:10.5px}
.top-bar .call{left:153px;top:8px}
.top-bar .follow{left:694px;top:8px;color:#c9d6e3}
.social{top:8px;width:13px;height:13px;border-radius:2px}

.header{left:0;top:30px;width:989px;height:103px;background:var(--header)}
.brand-mark{left:153px;top:57px;width:20px;height:20px;border-radius:50%;background:var(--yellow)}
.brand-name{left:180px;top:57px;color:#fff;font-size:14px;font-weight:600;line-height:20px;white-space:nowrap}
.brand-divider{left:276px;top:45px;width:1px;height:46px;background:#5c86ad}
.location{left:288px;top:58px;color:#fff;font-size:13.5px;letter-spacing:.3px}
.translate{left:719px;top:46px;width:117px;height:19px;background:#fff;border-radius:3px;font-size:8.5px;font-weight:700;color:#333;padding:4px 0 0 28px}
.translate .flag{position:absolute;left:6px;top:5px;width:16px;height:10px;background:linear-gradient(90deg,#1f3e9a 33%,#fff 33% 66%,#d32 66%)}
.translate svg{position:absolute;right:5px;top:6px}
.nav-home{left:261px;top:105px;width:66px;height:20px;background:var(--yellow);transform:skewX(-25deg)}
.nav-home-label{left:261px;top:108px;width:66px;text-align:center;color:#fff;font-weight:700;font-size:11px}
.nav{left:338px;top:110px;display:flex;gap:13px;color:#fff;font-size:10.5px;white-space:nowrap}

.hero{left:0;top:138px;width:989px;height:310px;background:linear-gradient(90deg,#8a7658 0%,#d7cbb6 28%,#9a8e7a 55%,#c2b49a 78%,#7c6a50 100%)}
.hero-arrow{top:256px;width:18px;height:74px;background:#333}
.hero-arrow svg{position:absolute;left:5px;top:32px}

.welcome{left:0;top:448px;width:989px;height:120px;background:var(--band);text-align:center}
.welcome h1{position:absolute;left:0;top:15px;width:989px;font-family:Ubuntu,sans-serif;font-weight:500;font-size:21px;color:var(--welcome-orange);letter-spacing:.5px}
.welcome p{position:absolute;left:185px;top:55px;width:620px;font-size:10px;line-height:14px;color:#666}

.section-title{font-family:Ubuntu,sans-serif;font-weight:500;font-size:16px;color:var(--orange)}
.col-rule{width:1px;background:#e4e4e4}

.offer-thumb{left:153px;width:66px;height:62px}
.offer-title{left:226px;font-family:Ubuntu,sans-serif;font-weight:500;font-size:12.5px;color:var(--link-blue)}
.offer-text{left:226px;width:150px;font-size:9px;line-height:12px;color:#555}

.review-frame{left:402px;top:633px;width:212px;height:121px;border:4px solid var(--frame);background:#fff}
.review-badge{left:468px;top:645px;width:80px;height:66px;border-radius:8px;background:#e3d8b8}
.review-text{left:402px;top:766px;width:215px;font-size:9.5px;line-height:13px;color:#444}
.btn{background:var(--yellow);color:#fff;font-weight:700;border-radius:3px;text-align:center;box-shadow:0 2px 0 #c98a10}
.read-more{left:403px;top:817px;width:67px;height:22px;font-size:9.5px;line-height:22px}

.field-label{left:644px;font-size:12px;color:#555}
.field{left:644px;height:20px;background:var(--input);border:1px solid #d2d2d2}
.field .cal{position:absolute;right:4px;top:5px}
.search{left:643px;top:817px;width:124px;height:23px;font-size:12px;line-height:23px;font-family:Ubuntu,sans-serif;font-weight:500}

.gallery-band{left:0;top:864px;width:989px;height:278px;background:var(--gallery-bg)}
.thumb{width:139px;height:80px;background:var(--frame);padding:4px}
.thumb div{width:100%;height:100%}
.pager{top:1105px;width:8px;height:8px;background:#111}
.map{left:626px;top:930px;width:210px;height:115px;background:var(--frame);padding:4px}
.map div{width:100%;height:100%;background:linear-gradient(135deg,#e9e5dc 0%,#f1ede4 40%,#cfe0bf 70%,#ece7de 100%)}
.address{left:626px;top:1056px;font-size:9px;line-height:14px;color:#444}

.footer{left:0;top:1142px;width:989px;height:58px;background:var(--footer);color:#fff}
.footer-nav{left:153px;top:1157px;font-size:8.5px;white-space:nowrap;color:#fff}
.footer-nav span{color:#aaa;margin:0 4px}
.copyright{left:154px;top:1180px;font-size:8.5px;color:#bbb}
.footer-mark{left:688px;top:1159px;width:14px;height:14px;border-radius:50%;background:var(--yellow)}
.footer-name{left:708px;top:1158px;font-size:10px;font-weight:600;line-height:16px;color:#fff;white-space:nowrap}
.footer-divider{left:780px;top:1148px;width:1px;height:40px;background:#555}
.footer-location{left:790px;top:1158px;font-size:11px;color:#ccc}
</style>
</head>
<body>
<div class="page">

  <div class="abs top-bar">
    <span class="abs call">CALL: + 44 (0) 20 7946 0321</span>
    <span class="abs follow">FOLLOW US:</span>
    <span class="abs social" style="left:758px;background:#3b5998"></span>
    <span class="abs social" style="left:774px;background:#39a6dd"></span>
    <span class="abs social" style="left:790px;background:#5a9e3a"></span>
    <span class="abs social" style="left:806px;background:#d6402f"></span>
    <span class="abs social" style="left:822px;background:#c9252f"></span>
  </div>

  <header class="abs header"></header>
  <div class="abs brand-mark"></div>
  <div class="abs brand-name">Restwell Inn</div>
  <div class="abs brand-divider"></div>
  <div class="abs location">London - Victoria</div>
  <div class="abs translate"><span class="flag"></span>TRANSLATE INTO
    <svg width="9" height="7" viewBox="0 0 9 7"><path d="M0 0h9L4.5 7z" fill="#2e6394"/></svg>
  </div>
  <div class="abs nav-home"></div>
  <div class="abs nav-home-label">HOME</div>
  <nav class="abs nav">
    <span>OUR ROOMS</span><span>ATTRACTIONS</span><span>LONDON EVENTS</span><span>SPECIAL OFFERS</span><span>PHOTOS</span><span>DIRECTIONS</span><span>CONTACT</span>
  </nav>

  <div class="abs hero" role="img" aria-label="Hotel bedroom with double bed, armchairs and table lamps"></div>
  <div class="abs hero-arrow" style="left:6px"><svg width="8" height="10" viewBox="0 0 8 10"><path d="M6 1L2 5l4 4" stroke="#fff" stroke-width="2" fill="none"/></svg></div>
  <div class="abs hero-arrow" style="left:965px"><svg width="8" height="10" viewBox="0 0 8 10"><path d="M2 1l4 4-4 4" stroke="#fff" stroke-width="2" fill="none"/></svg></div>

  <section class="abs welcome">
    <h1>WELCOME TO RESTWELL INN</h1>
    <p>Enjoy your stay at Restwell Inn Victoria and be sure that you’ve found our best value on the Internet. We always have some exclusive special offers for our guests.Stay with us and get 25% off on Spa Treatments. Linden Spa is a sanctuary of calm within luxurious and tranquil surroundings.</p>
  </section>

  <div class="abs col-rule" style="left:388px;top:585px;height:262px"></div>
  <div class="abs col-rule" style="left:617px;top:585px;height:262px"></div>

  <h2 class="abs section-title" style="left:153px;top:596px">SPECIAL OFFERS</h2>
  <div class="abs offer-thumb" style="top:633px;background:linear-gradient(135deg,#8d949a,#5a5f63)" role="img" aria-label="Silver hatchback car parked on a street"></div>
  <div class="abs offer-title" style="top:634px">Low Cost Car Hire</div>
  <div class="abs offer-text" style="top:654px">Hire a car, get a decent road map and getting from A to B won’t be as hard as you think.</div>
  <div class="abs offer-thumb" style="top:705px;background:linear-gradient(135deg,#b9a78e,#6d6253)" role="img" aria-label="Busy London shopping street"></div>
  <div class="abs offer-title" style="top:705px">Shopping in London</div>
  <div class="abs offer-text" style="top:728px">For the ultimate discount sales ping London is always one of the best cities to find bargains aplenty</div>
  <div class="abs offer-thumb" style="top:776px;background:radial-gradient(circle at 50% 45%,#d9a73c,#3b2a12 70%)" role="img" aria-label="Concert hall lit up at night"></div>
  <div class="abs offer-title" style="top:776px">Sunday Special</div>
  <div class="abs offer-text" style="top:798px">Discount up to £10 when you stay with us for the night of Sunday.</div>

  <h2 class="abs section-title" style="left:403px;top:596px">JOURNEYSCOPE REVIEWS</h2>
  <div class="abs review-frame"></div>
  <div class="abs review-badge"></div>
  <div class="abs" style="left:402px;top:724px;width:212px;text-align:center;font-size:15px;color:#222">Journeyscope</div>
  <p class="abs review-text">Stayed with us before?Want to view experiences from our previous guest? Read reviews on our Journeyscope page.</p>
  <div class="abs btn read-more">READ MORE</div>

  <h2 class="abs section-title" style="left:644px;top:596px">BOOKING CALENDER</h2>
  <div class="abs field-label" style="top:630px">From</div>
  <div class="abs field" style="top:649px;width:192px"><svg class="cal" width="12" height="9" viewBox="0 0 12 9"><rect width="12" height="9" fill="#999"/><rect x="1" y="3" width="10" height="5" fill="#eee"/><rect y="0" width="12" height="2" fill="#c33"/></svg></div>
  <div class="abs field-label" style="top:674px">To</div>
  <div class="abs field" style="top:693px;width:192px"><svg class="cal" width="12" height="9" viewBox="0 0 12 9"><rect width="12" height="9" fill="#999"/><rect x="1" y="3" width="10" height="5" fill="#eee"/><rect y="0" width="12" height="2" fill="#c33"/></svg></div>
  <div class="abs field-label" style="top:718px">Children</div>
  <div class="abs field" style="top:737px;width:100px"></div>
  <div class="abs field-label" style="top:762px">Adults</div>
  <div class="abs field" style="top:782px;width:69px"></div>
  <div class="abs btn search">Search Availability</div>

  <div class="abs gallery-band"></div>
  <h2 class="abs section-title" style="left:153px;top:888px">PHOTO GELLERY</h2>
  <div class="abs thumb" style="left:153px;top:930px"><div style="background:linear-gradient(135deg,#c9a36a,#7a2a22)" role="img" aria-label="Double bed with red throw"></div></div>
  <div class="abs thumb" style="left:298px;top:930px"><div style="background:linear-gradient(180deg,#9c8565,#4a4440)" role="img" aria-label="Hotel exterior on a terraced street"></div></div>
  <div class="abs thumb" style="left:444px;top:930px"><div style="background:linear-gradient(135deg,#b7a12a,#c45a6a 60%,#3a3a3a)" role="img" aria-label="Colourful cushions on a sofa"></div></div>
  <div class="abs thumb" style="left:153px;top:1015px"><div style="background:linear-gradient(135deg,#d7b690,#8a4a22)" role="img" aria-label="Breakfast room with tables"></div></div>
  <div class="abs thumb" style="left:298px;top:1015px"><div style="background:linear-gradient(135deg,#f0f0f0,#c9cfd2)" role="img" aria-label="White bathroom with basin and shower"></div></div>
  <div class="abs thumb" style="left:444px;top:1015px"><div style="background:linear-gradient(135deg,#d9cfc2,#9a7a55)" role="img" aria-label="Kitchen and dining area"></div></div>
  <div class="abs pager" style="left:545px;background:#2e6394"></div>
  <div class="abs pager" style="left:555px"></div>
  <div class="abs pager" style="left:565px"></div>
  <div class="abs pager" style="left:575px"></div>

  <div class="abs col-rule" style="left:604px;top:895px;height:210px;background:#dedede"></div>
  <h2 class="abs section-title" style="left:626px;top:888px">LOCATION MAP</h2>
  <div class="abs map"><div role="img" aria-label="Street map of the area around the hotel"></div></div>
  <address class="abs address" style="font-style:normal">
    12-16 Linden Row, Victoria London SW1X 0AA<br>
    stay@restwellmarlow.co.uk<br>
    TEL: + 44 (0) 20 7946 0321<br>
    &nbsp;FAX:+ 44 (0) 20 7946 0587
  </address>

  <footer class="abs footer"></footer>
  <div class="abs footer-nav">HOME<span>|</span>OUR ROOMS<span>|</span>ATTRACTIONS<span>|</span>LONDON EVENTS<span>|</span>SPECIAL OFFERS<span>|</span>PHOTOS<span>|</span>DIRECTIONS<span>|</span>CONTACT</div>
  <div class="abs copyright">© 2013. ALL RIGHTS RESERVED.</div>
  <div class="abs footer-mark"></div>
  <div class="abs footer-name">Restwell Inn</div>
  <div class="abs footer-divider"></div>
  <div class="abs footer-location">London - Victoria</div>

</div>
</body>
</html>
```